pop up booking component and calendar re-design

we have a calander view where a parent cant reserve a day
you can click on please redesign the calander / voucher and pop up.

the dropdowns in pop up can be buttons
the dots on the calander indicate if there is space or not

when booking a day you can select a voucher

we used KIVO as inspiration, you are welcome to look at it as well.. screenshots attached

please ask questions if you have any

```html
<!DOCTYPE html>
<html lang="en">
<head>
<meta charset="utf-8">
<title>Day Booking – Calendar and Pop-up</title>
<link href="https://fonts.googleapis.com/css2?family=Roboto:wght@400;500;700&display=swap" rel="stylesheet">
<style>
  :root{
    --canvas:#eeebe6;
    --yellow-top:#ffd62a;
    --yellow-bottom:#ffb400;
    --orange:#f5a300;
    --orange-soft:#f7c25a;
    --ink:#1d1d1f;
    --ink-soft:#4a4a4f;
    --muted:#a3a3a8;
    --line:#e4e4e8;
    --blue:#2f6fe3;
    --white:#ffffff;
    --overlay:#8c8c8e;
    --map:#e3e6f3;
    --pill-dark:#141414;
  }
  *{box-sizing:border-box;margin:0;padding:0}
  html,body{width:1200px;height:800px;overflow:hidden}
  body{background:var(--canvas);font-family:"Roboto",sans-serif;color:var(--ink);position:relative}

  .screen{position:absolute;top:30px;width:340px;height:740px;background:var(--white);overflow:hidden;border-radius:18px;box-shadow:0 6px 24px rgba(0,0,0,.12)}
  .screen--ride{left:30px;background:var(--map)}
  .screen--calendar{left:430px}
  .screen--booking{left:830px}

  .status-bar{position:absolute;top:0;left:0;right:0;height:34px;display:flex;align-items:center;justify-content:space-between;padding:0 16px 0 18px;font-size:14px;font-weight:500;z-index:3}
  .status-icons{display:flex;gap:5px;align-items:center}

  /* header */
  .app-header{position:absolute;top:0;left:0;right:0;height:127px;background:linear-gradient(var(--yellow-top),var(--yellow-bottom))}
  .month-pill{position:absolute;top:40px;left:48px;width:244px;height:28px;border-radius:14px;background:var(--white);font-size:12px;display:flex;align-items:center;justify-content:center}
  .month-pill svg{position:absolute;right:10px;top:8px}
  .nav-arrow{position:absolute;top:44px}
  .nav-arrow--prev{left:16px}
  .nav-arrow--next{right:16px}
  .view-tabs{position:absolute;top:88px;left:0;right:0;display:flex;justify-content:center;gap:16px;font-size:11.5px;color:rgba(255,255,255,.85)}
  .view-tabs .is-active{color:var(--ink);font-weight:700}

  /* calendar */
  .calendar{position:absolute;top:136px;left:18px;width:304px}
  .weekdays,.dates{display:grid;grid-template-columns:repeat(7,1fr);text-align:center}
  .weekdays{font-size:10.5px;margin-bottom:8px}
  .weekend{color:var(--orange)}
  .dates{grid-template-rows:40px 40px 80px 40px 40px 40px;font-size:14.5px}
  .day{position:relative;display:flex;justify-content:center;padding-top:2px}
  .day--faded{color:var(--muted)}
  .day--faded.weekend{color:#d5d5d8}
  .day--today span{background:var(--orange);color:var(--white);border-radius:4px;padding:1px 4px}
  .day-tile{width:38px;height:62px;background:var(--blue);color:var(--white);border-radius:3px;text-align:left;padding:2px 4px;font-size:14px;line-height:1.1}
  .day-tile small{display:block;font-size:4.2px;line-height:1.35;margin-top:4px}
  .dot{display:block;width:5px;height:5px;border-radius:50%;margin-top:2px}
  .dot--full{background:#13204a}
  .dot--space{background:var(--yellow-top)}

  .circle-btn{position:absolute;top:460px;width:32px;height:32px;border-radius:50%;display:flex;align-items:center;justify-content:center}
  .circle-btn--up{left:22px;background:var(--white);box-shadow:0 1px 5px rgba(0,0,0,.18)}
  .circle-btn--refresh{right:22px;background:var(--orange)}

  .booking-card{position:absolute;top:514px;left:24px;width:290px;height:84px;background:var(--white);box-shadow:0 2px 10px rgba(0,0,0,.14);border-radius:3px;display:flex;padding:12px}
  .booking-card__date{width:70px;border-right:1px solid var(--line);padding-right:8px}
  .booking-card__date strong{display:block;font-size:22px;color:var(--blue);font-weight:700}
  .booking-card__date span{display:block;font-size:6.5px;line-height:1.3;margin-top:4px}
  .booking-card__note{font-size:6.3px;line-height:1.75;padding-left:12px;color:var(--ink-soft)}

  .action-links{position:absolute;top:638px;left:24px;width:290px;display:flex;justify-content:space-between;font-size:14px;color:var(--muted)}
  .action-links span{flex:1;text-align:center}
  .action-links span+span{border-left:1px solid var(--line)}
  .primary-btn{position:absolute;left:24px;width:290px;height:42px;border-radius:3px;background:linear-gradient(var(--yellow-top),var(--yellow-bottom));color:var(--white);font-size:14.5px;font-weight:500;display:flex;align-items:center;justify-content:center}
  .screen--calendar .primary-btn,.screen--booking .footer-btn{top:680px}

  /* booking overlay */
  .dim-layer{position:absolute;top:127px;left:0;right:0;bottom:0;background:var(--overlay)}
  .screen--booking .action-links{color:#6e6e72}
  .screen--booking .action-links span+span{border-left-color:#777}
  .footer-btn{background:#7a7a7c;color:#999;border:1px solid #6a6a6c}
  .modal{position:absolute;top:145px;left:29px;width:285px;height:448px;background:var(--white);border-radius:3px;box-shadow:0 4px 14px rgba(0,0,0,.2);font-size:9px}
  .modal-tabs{display:flex;height:40px;border-bottom:1px solid var(--line)}
  .modal-tabs span{flex:1;text-align:center;padding-top:14px;font-size:12px;color:var(--muted)}
  .modal-tabs .is-active{color:var(--ink);font-weight:500;border-bottom:2px solid var(--orange)}
  .availability{text-align:center;font-size:6.5px;margin-top:17px;color:var(--ink-soft);padding-bottom:8px;border-bottom:1px solid var(--line);margin-left:12px;margin-right:12px}
  .field-labels{position:absolute;top:90px;left:18px;display:flex;font-size:10.5px;color:var(--ink-soft)}
  .field-labels span{width:98px}
  .field-labels i{color:var(--orange);font-style:normal}
  .field{position:absolute;top:108px;width:78px;height:31px;border-radius:3px;box-shadow:0 1px 4px rgba(0,0,0,.18);font-size:7.5px;display:flex;align-items:center;padding-left:9px}
  .field--location{left:12px}
  .field--group{left:97px}
  .field--group svg{position:absolute;right:9px;top:13px}
  .toggle{position:absolute;top:113px;left:199px;width:42px;height:22px;border-radius:11px;background:#7d7d80}
  .toggle::after{content:"";position:absolute;top:3px;left:3px;width:16px;height:16px;border-radius:50%;background:var(--white)}
  .option-btn{position:absolute;height:31px;border:1.4px solid var(--orange-soft);border-radius:3px;color:var(--orange);font-size:7px;font-weight:700;display:flex;align-items:center;padding-left:8px}
  .modal .primary-btn{left:12px;width:261px;height:43px}
  .restart-btn{top:239px}
  .confirm-btn{top:390px}
  .price-box{position:absolute;top:293px;left:12px;width:261px;height:84px;border:1px solid var(--line);border-radius:3px;font-size:7px}
  .price-row{display:flex;justify-content:space-between;align-items:center;height:27px;padding:0 10px;color:var(--muted)}
  .price-row+.price-row{border-top:1px solid var(--line)}
  .price-row--total{color:var(--ink);font-weight:700}
  .apply-pill{background:var(--blue);color:var(--white);border-radius:6px;padding:1px 8px;font-size:6px}

  /* ride screen */
  .map-area{position:absolute;inset:0;background:linear-gradient(160deg,#e8ebf6,#dfe2f0 60%,#d8dcec)}
  .route-card{position:absolute;top:46px;left:14px;width:312px;height:50px;border-radius:25px;background:linear-gradient(90deg,var(--yellow-bottom),var(--yellow-top));padding:10px 0 0 40px;z-index:2}
  .route-card b{display:block;font-size:12px;color:#fff7d8;font-weight:700}
  .route-card span{font-size:9px}
  .route-card .back{position:absolute;left:16px;top:18px}
  .route-card .close{position:absolute;right:20px;top:20px}
  .stop{position:absolute;left:22px;width:296px;height:34px;background:var(--white);border-radius:3px;font-size:8px;display:flex;align-items:center;padding-left:28px;z-index:2;box-shadow:0 1px 3px rgba(0,0,0,.06)}
  .stop::before{content:"";position:absolute;left:11px;top:14px;width:6px;height:6px;border-radius:50%;background:var(--ink)}
  .stop svg{position:absolute;right:14px;top:12px}
  .stop--from{top:102px}
  .stop--to{top:140px}
  .place-pill{position:absolute;top:248px;left:34px;width:196px;height:30px;border-radius:15px;background:var(--pill-dark);color:var(--white);font-size:11px;font-weight:500;display:flex;align-items:center;padding-left:14px}
  .place-pill svg{position:absolute;right:12px;top:10px}
  .ride-sheet{position:absolute;top:498px;left:0;right:0;bottom:0;background:var(--white);border-radius:16px 16px 0 0}
  .ride-option{position:absolute;top:14px;left:14px;width:206px;height:84px;border-radius:6px;box-shadow:0 1px 6px rgba(0,0,0,.1);padding:10px 12px}
  .car-badge{display:inline-flex;width:28px;height:28px;border-radius:50%;background:#6b6b70;align-items:center;justify-content:center;vertical-align:middle}
  .eta{font-size:12px;font-weight:700;margin-left:44px;vertical-align:middle}
  .ride-name{display:block;color:var(--orange);font-size:11px;font-weight:700;margin-top:6px}
  .ride-meta{font-size:7.5px;color:var(--ink-soft)}
  .ride-meta small{display:block;font-size:5.5px;color:var(--muted)}
  .fare-chip{position:absolute;top:14px;left:228px;width:98px;height:40px;border-radius:6px;background:linear-gradient(var(--yellow-top),var(--yellow-bottom));font-size:8px;font-weight:700;display:flex;align-items:center;justify-content:center}
  .tool{position:absolute;top:60px;width:48px;height:38px;border-radius:6px;box-shadow:0 1px 6px rgba(0,0,0,.1);font-size:7px;display:flex;flex-direction:column;align-items:center;justify-content:center;gap:3px}
  .tool--options{left:228px}
  .tool--personal{left:280px}
  .fare-summary{position:absolute;top:112px;left:0;right:0;text-align:center}
  .fare-summary .currency{color:var(--orange);font-size:10px;font-weight:500}
  .fare-summary .amount{font-size:16px;font-weight:700;margin:0 6px}
  .fare-summary s{color:var(--muted);font-size:13px}
  .fare-summary p{font-size:8.5px;color:var(--ink-soft);margin-top:4px}
  .book-btn{position:absolute;top:180px;left:14px;width:312px;height:44px;border-radius:4px;background:linear-gradient(var(--yellow-top),var(--yellow-bottom));color:#fff7d8;font-size:14px;font-weight:700;display:flex;align-items:center;justify-content:center}
</style>
</head>
<body>

<!-- Ride app screen -->
<section class="screen screen--ride">
  <div class="map-area" role="img" aria-label="Street map of the neighbourhood with nearby places and the planned route"></div>
  <div class="status-bar"><span>12:01 ➚</span><span class="status-icons">
    <svg width="16" height="10"><rect x="0" y="6" width="3" height="4"/><rect x="4" y="4" width="3" height="6"/><rect x="8" y="2" width="3" height="8"/><rect x="12" y="0" width="3" height="10"/></svg>
    <svg width="20" height="10"><rect x="0.5" y="0.5" width="17" height="9" rx="2" fill="none" stroke="#1d1d1f"/><rect x="2" y="2" width="10" height="6" fill="#1d1d1f"/></svg></span></div>
  <div class="route-card">
    <svg class="back" width="8" height="12"><path d="M7 1L2 6l5 5" stroke="#1d1d1f" stroke-width="1.5" fill="none"/></svg>
    <b>Gym</b><span>East Entrance</span>
    <svg class="close" width="9" height="9"><path d="M1 1l7 7M8 1L1 8" stroke="#fff" stroke-width="1.5"/></svg>
  </div>
  <div class="stop stop--from">ABC Street 12345<svg width="9" height="9"><path d="M1 1l7 7M8 1L1 8" stroke="#1d1d1f" stroke-width="1.4"/></svg></div>
  <div class="stop stop--to">DEF Street 12345<svg width="9" height="9"><path d="M1 1l7 7M8 1L1 8" stroke="#1d1d1f" stroke-width="1.4"/></svg></div>
  <div class="place-pill">Lindenhof Residences<svg width="7" height="11"><path d="M1 1l5 4.5L1 10" stroke="#fff" stroke-width="1.5" fill="none"/></svg></div>
  <div class="ride-sheet">
    <div class="ride-option">
      <span class="car-badge"><svg width="18" height="10"><path d="M2 7h14l-2-5H5z" fill="#fff"/><circle cx="5" cy="8" r="1.6" fill="#333"/><circle cx="13" cy="8" r="1.6" fill="#333"/></svg></span>
      <span class="eta">1-3 Min</span>
      <span class="ride-name">JustKivo</span>
      <div class="ride-meta">1-4 seats<small>Find the nearest car or taxi</small></div>
    </div>
    <div class="fare-chip">RM 24.66</div>
    <div class="tool tool--options"><svg width="22" height="6"><circle cx="3" cy="3" r="2.3" fill="none" stroke="#1d1d1f"/><circle cx="11" cy="3" r="2.3" fill="none" stroke="#1d1d1f"/><circle cx="19" cy="3" r="2.3" fill="none" stroke="#1d1d1f"/></svg>Options</div>
    <div class="tool tool--personal"><svg width="12" height="12"><circle cx="6" cy="3.5" r="2.8" fill="none" stroke="#1d1d1f"/><path d="M1 12c0-3 2.2-5 5-5s5 2 5 5" fill="none" stroke="#1d1d1f"/></svg>Personal</div>
    <div class="fare-summary">
      <span class="currency">RM</span><span class="amount">11</span><s>14</s>
      <p>Fares are higher due to high demand</p>
    </div>
    <div class="book-btn">Book</div>
  </div>
</section>

<!-- Calendar screen -->
<section class="screen screen--calendar">
  <header class="app-header">
    <div class="status-bar"><span>12:01 ➚</span><span class="status-icons">
      <svg width="16" height="10"><rect x="0" y="6" width="3" height="4"/><rect x="4" y="4" width="3" height="6"/><rect x="8" y="2" width="3" height="8"/><rect x="12" y="0" width="3" height="10"/></svg>
      <svg width="20" height="10"><rect x="0.5" y="0.5" width="17" height="9" rx="2" fill="none" stroke="#1d1d1f"/><rect x="2" y="2" width="10" height="6" fill="#1d1d1f"/></svg></span></div>
    <svg class="nav-arrow nav-arrow--prev" width="10" height="16"><path d="M8 1L2 8l6 7" stroke="#1d1d1f" stroke-width="1.6" fill="none"/></svg>
    <div class="month-pill">Novmeber 2019<svg width="12" height="12"><circle cx="3" cy="3" r="2.2" fill="none" stroke="#999"/><circle cx="9" cy="3" r="2.2" fill="none" stroke="#999"/><circle cx="3" cy="9" r="2.2" fill="none" stroke="#999"/><circle cx="9" cy="9" r="2.2" fill="none" stroke="#999"/></svg></div>
    <svg class="nav-arrow nav-arrow--next" width="10" height="16"><path d="M2 1l6 7-6 7" stroke="#1d1d1f" stroke-width="1.6" fill="none"/></svg>
    <nav class="view-tabs"><span>Today</span><span class="is-active">Day</span><span>Week</span><span>Month</span></nav>
  </header>

  <div class="calendar">
    <div class="weekdays"><span>MON</span><span>TUE</span><span>WED</span><span>THU</span><span>FRI</span><span class="weekend">SAT</span><span class="weekend">SUN</span></div>
    <div class="dates">
      <span class="day">30</span><span class="day">1</span><span class="day">2</span><span class="day">3</span><span class="day">4</span><span class="day weekend">5</span><span class="day weekend">6</span>
      <span class="day">7</span><span class="day">8</span><span class="day">9</span><span class="day day--today"><span>10</span></span><span class="day">11</span><span class="day weekend">12</span><span class="day weekend">13</span>
      <span class="day"><span class="day-tile">14<i class="dot dot--full"></i><small>RBW<br>PENGUINS<br>07:30 - 18:30<br>98.23</small></span></span>
      <span class="day">15</span><span class="day">16</span>
      <span class="day"><span class="day-tile">17<i class="dot dot--space"></i><small>RBW<br>PENGUINS<br>07:30 - 18:30<br>98.23</small></span></span>
      <span class="day">18</span><span class="day weekend">19</span><span class="day weekend">20</span>
      <span class="day">21</span><span class="day">22</span><span class="day">23</span><span class="day">24</span><span class="day">25</span><span class="day weekend">26</span><span class="day weekend">27</span>
      <span class="day">28</span><span class="day">29</span><span class="day">30</span><span class="day">31</span><span class="day">1</span><span class="day weekend">2</span><span class="day weekend">3</span>
      <span class="day day--faded">4</span><span class="day day--faded">5</span><span class="day day--faded">6</span><span class="day day--faded">7</span><span class="day day--faded">8</span><span class="day day--faded weekend">9</span><span class="day day--faded weekend">10</span>
    </div>
  </div>

  <span class="circle-btn circle-btn--up"><svg width="12" height="8"><path d="M1 7l5-5 5 5" stroke="#f5a300" stroke-width="1.5" fill="none"/></svg></span>
  <span class="circle-btn circle-btn--refresh"><svg width="16" height="16"><path d="M13 8a5 5 0 1 1-2-4" stroke="#fff" stroke-width="1.6" fill="none"/><path d="M11 1v3.5h-3.5" stroke="#fff" stroke-width="1.6" fill="none"/></svg></span>

  <article class="booking-card">
    <div class="booking-card__date"><strong>17</strong><span>RBW PENGUINS<br>07:30 - 18:30<br>98.23</span></div>
    <p class="booking-card__note">Lorem Ipsum has been the industry's standard dummy text ever since the 1500s, when an unknown printer took a galley of type and scrambled it to make a type specimen book.</p>
  </article>

  <div class="action-links"><span>Not Coming</span><span>Unselect</span><span>Cancel</span></div>
  <div class="primary-btn">Vouchers / Promotions</div>
</section>

<!-- Booking pop-up screen -->
<section class="screen screen--booking">
  <header class="app-header">
    <div class="status-bar"><span>12:01 ➚</span><span class="status-icons">
      <svg width="16" height="10"><rect x="0" y="6" width="3" height="4"/><rect x="4" y="4" width="3" height="6"/><rect x="8" y="2" width="3" height="8"/><rect x="12" y="0" width="3" height="10"/></svg>
      <svg width="20" height="10"><rect x="0.5" y="0.5" width="17" height="9" rx="2" fill="none" stroke="#1d1d1f"/><rect x="2" y="2" width="10" height="6" fill="#1d1d1f"/></svg></span></div>
    <svg class="nav-arrow nav-arrow--prev" width="10" height="16"><path d="M8 1L2 8l6 7" stroke="#1d1d1f" stroke-width="1.6" fill="none"/></svg>
    <div class="month-pill">Novmeber 2019<svg width="12" height="12"><circle cx="3" cy="3" r="2.2" fill="none" stroke="#999"/><circle cx="9" cy="3" r="2.2" fill="none" stroke="#999"/><circle cx="3" cy="9" r="2.2" fill="none" stroke="#999"/><circle cx="9" cy="9" r="2.2" fill="none" stroke="#999"/></svg></div>
    <svg class="nav-arrow nav-arrow--next" width="10" height="16"><path d="M2 1l6 7-6 7" stroke="#1d1d1f" stroke-width="1.6" fill="none"/></svg>
    <nav class="view-tabs"><span>Today</span><span class="is-active">Day</span><span>Week</span><span>Month</span></nav>
  </header>
  <div class="dim-layer"></div>
  <div class="action-links"><span>Not Coming</span><span>Unselect</span><span>Cancel</span></div>
  <div class="primary-btn footer-btn">Vouchers / Promotions</div>

  <div class="modal">
    <div class="modal-tabs"><span class="is-active">Book Day</span><span>Vouchers</span></div>
    <p class="availability">Availability - &nbsp;1m/1a left 24-10-2019</p>
    <div class="field-labels"><span>LOCATIONS<i>*</i></span><span>GROUPS<i>*</i></span><span>BSO</span></div>
    <div class="field field--location">RBW</div>
    <div class="field field--group">3-Penguins<svg width="6" height="4"><path d="M0 0h6L3 4z" fill="#1d1d1f"/></svg></div>
    <span class="toggle"></span>
    <span class="option-btn" style="top:152px;left:12px;width:80px">FULL</span>
    <span class="option-btn" style="top:152px;left:102px;width:80px">AM</span>
    <span class="option-btn" style="top:152px;left:192px;width:81px">PM</span>
    <span class="option-btn" style="top:194px;left:12px;width:125px">FLEX</span>
    <span class="option-btn" style="top:194px;left:148px;width:125px">TRY</span>
    <div class="primary-btn restart-btn">Restart</div>
    <div class="price-box">
      <div class="price-row"><span>Price</span><span>€ 98.23</span></div>
      <div class="price-row"><span>Voucher</span><span class="apply-pill">Apply</span></div>
      <div class="price-row price-row--total"><span>Total</span><span>€ 98.23</span></div>
    </div>
    <div class="primary-btn confirm-btn">Confirm</div>
  </div>
</section>

</body>
</html>
```